TARPLOAD business card design

TARPLOAD is a manufacturer of skip bags supplying both the domestic and commercial market. We wish to convey core characteristics of strength, professionalism and reliability to our customers. We are after a business card that uses our company colours of black and yellow as well as incorporating our logo. Our customers are predominantly in the construction or hardware industry. It is important the cards are professional as we are a small company wishing to appear larger than we actually are. more info on the company and product available at www.tarpload-example.com.au

Target Market(s)

hardware buyers, contruction company owners

Industry/Entity Type

Construction

Requirements
Must have
• company colours of black and yellow - No other colours or variation of yellow black. our company logo. card design must convey "tough"
• Card design must be landscape
• Details to be included on the card are:
• Name and Tiltle
• Phone number : 1300 41 62 53
• Mobile: 0452 718 903
• Fax: 03 9617 4852
• email: dale.hendry@tarpload-example.com.au
• address: PO Box 517, Kelvindale, VIC,3294
• Text in white when on a black background
Nice to have
• I like the idea of the back of the card being black with lighter circle area in the middle with black logo in the centre. Similar to the attached "iconic" card

```html
<!DOCTYPE html>
<html lang="en">
<head>
<meta charset="utf-8">
<title>TARPLOAD Business Card</title>
<link href="https://fonts.googleapis.com/css2?family=Anton&family=Oswald:wght@500&display=swap" rel="stylesheet">
<style>
  :root {
    --page: #ffffff;
    --card-black: #000000;
    --glow: #3a3a3a;
    --brand-yellow: #f2c500;
    --ink-black: #000000;
    --ink-white: #ffffff;
  }
  * { margin: 0; padding: 0; box-sizing: border-box; }
  html, body {
    width: 1200px;
    height: 1184px;
    overflow: hidden;
    background: var(--page);
  }
  .canvas {
    position: relative;
    width: 1200px;
    height: 1184px;
  }
  .card {
    position: absolute;
    width: 810px;
    height: 496px;
  }
  .card-back {
    left: 182px;
    top: 83px;
    background: radial-gradient(circle at 50% 48%, var(--glow) 0%, #1a1a1a 22%, var(--card-black) 48%);
  }
  .card-front {
    left: 180px;
    top: 627px;
    background: var(--brand-yellow);
  }
  .brand {
    position: absolute;
    left: 62px;
    top: 232px;
    display: flex;
    align-items: center;
    gap: 12px;
  }
  .brand-mark {
    width: 26px;
    height: 26px;
    background: var(--ink-black);
  }
  .brand-name {
    font-family: "Anton", sans-serif;
    font-size: 46px;
    line-height: 1;
    color: var(--ink-black);
    letter-spacing: 1px;
  }
  .details {
    position: absolute;
    left: 376px;
    top: 46px;
    color: var(--ink-white);
  }
  .person-name {
    font-family: "Anton", sans-serif;
    font-size: 50px;
    line-height: 1.1;
    letter-spacing: 1px;
  }
  .person-title {
    font-family: "Anton", sans-serif;
    font-size: 25px;
    line-height: 1;
    margin-top: 14px;
    letter-spacing: 0.5px;
  }
  .phones {
    list-style: none;
    margin-top: 42px;
    font-family: "Oswald", sans-serif;
    font-weight: 500;
    font-size: 22px;
    line-height: 35px;
  }
  .phones .label {
    display: inline-block;
    width: 34px;
  }
  .contact {
    list-style: none;
    margin-top: 20px;
    font-family: "Oswald", sans-serif;
    font-weight: 500;
    font-size: 22px;
    line-height: 35px;
  }
</style>
</head>
<body>
  <main class="canvas">
    <section class="card card-back" aria-label="Card back"></section>

    <section class="card card-front" aria-label="Card front">
      <div class="brand">
        <span class="brand-mark"></span>
        <span class="brand-name">TARPLOAD</span>
      </div>

      <div class="details">
        <h1 class="person-name">Dale Hendry</h1>
        <p class="person-title">Managing Director</p>
        <ul class="phones">
          <li><span class="label">P</span>: 1300 41 62 53</li>
          <li><span class="label">M</span>: 0452 718 903</li>
          <li><span class="label">F</span>: 03 9617 4852</li>
        </ul>
        <ul class="contact">
          <li>PO Box 517, Kelvindale, VIC, 3294</li>
          <li>dale.hendry@tarpload-example.com.au</li>
          <li>www.tarpload-example.com.au</li>
        </ul>
      </div>
    </section>
  </main>
</body>
</html>
```